Tarrowby Builders Business Card Design

We require a business Card for a new Building Company called Tarrowby Builders. We are General Builders that specialize in Industrial, Commercial and Domestic building work. We would like to see a design that incorporates Blue ,Red and White as the colour scheme and a design that will highlight a building theme.
(Once this design is achieved will need to incorporate this for the other side of the business which is Tarrowby Joinery )

Industry/Entity Type

Business

Contact Information for Business Card

TARROWBY BUILDERS
17 Wendalee Rd Kelbrook SA 5371
Mobile 0427390658
Telephone 08 85947316
Marcus Dewhirst
Director / Supervisor

```html
<!DOCTYPE html>
<html lang="en">
<head>
<meta charset="utf-8">
<title>Tarrowby Builders – Business Card</title>
<link rel="stylesheet" href="https://fonts.googleapis.com/css2?family=Open+Sans:wght@400;600;700&display=swap">
<style>
  :root {
    --brand-blue: #1565c0;
    --brand-blue-deep: #0d57ad;
    --brand-red: #e3262f;
    --card-white: #f7f7f7;
    --page-bg: #e6e3de;
    --band-text: #ffffff;
  }
  * { box-sizing: border-box; margin: 0; padding: 0; }
  html, body {
    width: 1200px; height: 780px; overflow: hidden;
    background: var(--page-bg);
    font-family: "Open Sans", Arial, sans-serif;
  }
  .canvas {
    width: 1200px; height: 780px;
    display: flex; align-items: center; justify-content: center; gap: 44px;
  }
  .card {
    position: relative;
    width: 540px; height: 310px;
    background: linear-gradient(135deg, #ffffff 0%, var(--card-white) 60%, #ececec 100%);
    box-shadow: 0 6px 18px rgba(0,0,0,.18);
    overflow: hidden;
  }
  .address-band {
    position: absolute; left: 0; right: 0; bottom: 0; height: 54px;
    background: var(--brand-blue);
    border-top: 6px solid var(--card-white);
    box-shadow: 0 -2px 0 0 var(--brand-red);
    display: flex; align-items: center; justify-content: center;
    color: var(--band-text); font-size: 17px; font-weight: 600; letter-spacing: .3px;
    white-space: nowrap;
  }
  .card-back .address-band { background: var(--brand-blue-deep); }

  /* ---------- front ---------- */
  .card-front .brand-mark {
    position: absolute; left: 36px; top: 60px; width: 220px; height: 150px;
    display: flex; flex-direction: column; align-items: center; justify-content: center; gap: 12px;
  }
  .brand-square { flex: none; width: 26px; height: 26px; background: var(--brand-red); }
  .brand-name {
    color: var(--brand-blue); font-weight: 700; font-size: 19px; line-height: 1.15;
    letter-spacing: .5px; white-space: nowrap;
  }
  .divider {
    position: absolute; left: 276px; top: 40px; width: 1.5px; height: 170px;
    background: var(--brand-blue);
  }
  .contact { position: absolute; left: 304px; top: 50px; }
  .person-name {
    color: var(--brand-blue); font-weight: 600; font-size: 24px; line-height: 1.1; white-space: nowrap;
  }
  .person-role { color: var(--brand-red); font-size: 14px; margin-top: 4px; }
  .phone-list { list-style: none; margin-top: 40px; }
  .phone-list li {
    display: flex; align-items: center; gap: 8px;
    color: var(--brand-blue); font-size: 17px; margin-bottom: 6px;
  }
  .phone-icon {
    flex: none; width: 17px; height: 17px; background: var(--brand-red);
    display: flex; align-items: center; justify-content: center; border-radius: 2px;
  }

  /* ---------- back ---------- */
  .card-back .brand-mark {
    position: absolute; left: 0; right: 0; top: 0; bottom: 54px;
    display: flex; align-items: center; justify-content: center; gap: 14px;
  }
  .card-back .brand-square { width: 30px; height: 30px; }
  .card-back .brand-name { font-size: 28px; }
</style>
</head>
<body>
<main class="canvas">
  <section class="card card-front" aria-label="Business card front">
    <div class="brand-mark">
      <span class="brand-square"></span>
      <span class="brand-name">TARROWBY BUILDERS</span>
    </div>
    <div class="divider"></div>
    <div class="contact">
      <p class="person-name">Marcus Dewhirst</p>
      <p class="person-role">Director / Supervisor</p>
      <ul class="phone-list">
        <li>
          <span class="phone-icon">
            <svg width="9" height="12" viewBox="0 0 9 12"><rect x="1" y="0.5" width="7" height="11" rx="1.2" fill="none" stroke="#fff" stroke-width="1.2"/><rect x="2.5" y="2" width="4" height="5" fill="#fff"/></svg>
          </span>
          0427390658
        </li>
        <li>
          <span class="phone-icon">
            <svg width="12" height="11" viewBox="0 0 12 11"><path d="M1 4 Q6 0 11 4 L9.5 5.5 L8 4.5 L8 3.5 Q6 2.8 4 3.5 L4 4.5 L2.5 5.5 Z" fill="#fff"/><rect x="2.5" y="6" width="7" height="4.5" rx=".8" fill="#fff"/></svg>
          </span>
          08 85947316
        </li>
      </ul>
    </div>
    <div class="address-band">17 Wendalee Rd Kelbrook SA 5371</div>
  </section>

  <section class="card card-back" aria-label="Business card back">
    <div class="brand-mark">
      <span class="brand-square"></span>
      <span class="brand-name">TARROWBY BUILDERS</span>
    </div>
    <div class="address-band">17 Wendalee Rd Kelbrook SA 5371</div>
  </section>
</main>
</body>
</html>
```